Parcels & Petals
Parcels & Petals - Gifts and Occasions
Creative Brief
Bright & Fun-filled
Ritu Malhotra
C-17, Dilkusha Marg Lucknow - 226014
ritumal47@postbright.example
www.parcelspetals.example
I want the logo on one side and the other details on the other side. The logo to be used is draft no. 3 in my project parcels and petals

```html
<!DOCTYPE html>
<html lang="en">
<head>
<meta charset="utf-8">
<title>Parcels &amp; Petals – Business Card</title>
<link rel="stylesheet" href="https://fonts.googleapis.com/css2?family=Nunito:wght@400;600;800&display=swap">
<style>
  :root {
    --backdrop: #e9ebee;
    --card-white: #ffffff;
    --card-shade: #f1f2f4;
    --band-blue: #5aaee2;
    --band-blue-deep: #4a9fd6;
    --ink-white: #ffffff;
    --brand-ink: #3f9ad6;
    --stripe-pink: #e8417c;
    --stripe-red: #e23a36;
    --stripe-yellow: #f5cf2a;
    --stripe-green: #7cc142;
    --stripe-orange: #f39a1f;
    --stripe-blue: #3f9ad6;
  }
  * { margin: 0; padding: 0; box-sizing: border-box; }
  html, body {
    width: 1200px; height: 838px; overflow: hidden;
    background: var(--backdrop);
    font-family: "Nunito", sans-serif;
  }
  .sheet {
    width: 1200px; height: 838px;
    display: flex; flex-direction: column; align-items: center; justify-content: center;
    gap: 28px;
  }
  .card {
    position: relative;
    width: 690px; height: 394px;
    border-radius: 16px;
    overflow: hidden;
    background: linear-gradient(180deg, var(--card-white) 0%, var(--card-white) 55%, var(--card-shade) 100%);
    box-shadow: 0 8px 24px rgba(0,0,0,0.12);
  }
  .brand {
    position: absolute; left: 0; right: 0;
    display: flex; align-items: center; justify-content: center; gap: 14px;
  }
  .brand-square {
    width: 26px; height: 26px; border-radius: 4px;
    background: var(--brand-ink);
  }
  .brand-name {
    font-weight: 800; font-size: 44px; letter-spacing: 0.5px;
    color: var(--brand-ink);
  }
  .card--back .brand { top: 0; bottom: 0; }
  .card--front .brand { top: 58px; }
  .color-stripe {
    position: absolute; left: 0; right: 0; top: 206px; height: 8px;
    display: flex;
  }
  .color-stripe span { flex: 1; }
  .color-stripe .s1 { background: var(--band-blue); flex: 1.4; }
  .color-stripe .s2 { background: var(--stripe-pink); }
  .color-stripe .s3 { background: var(--stripe-red); }
  .color-stripe .s4 { background: var(--stripe-yellow); }
  .color-stripe .s5 { background: var(--stripe-green); }
  .color-stripe .s6 { background: var(--stripe-orange); }
  .color-stripe .s7 { background: var(--stripe-blue); flex: 0.8; }
  .blue-band {
    position: absolute; left: 0; right: 0; top: 214px; bottom: 0;
    background: linear-gradient(180deg, var(--band-blue) 0%, var(--band-blue-deep) 100%);
    color: var(--ink-white);
  }
  .holder {
    position: absolute; left: 60px; top: 26px; width: 250px;
    text-align: right;
  }
  .holder-name { font-weight: 800; font-size: 24px; letter-spacing: 0.5px; }
  .holder-address { font-weight: 400; font-size: 15px; line-height: 1.45; margin-top: 14px; }
  .divider {
    position: absolute; left: 340px; top: 28px; width: 1px; height: 116px;
    background: rgba(255,255,255,0.55);
  }
  .contacts {
    position: absolute; left: 362px; top: 30px;
    list-style: none; font-size: 15px; line-height: 1;
  }
  .contacts li { display: flex; align-items: center; gap: 10px; margin-bottom: 14px; }
  .contacts svg { width: 16px; height: 16px; flex: none; }
</style>
</head>
<body>
  <main class="sheet">
    <section class="card card--back" aria-label="Card back">
      <div class="brand">
        <span class="brand-square"></span>
        <span class="brand-name">Parcels &amp; Petals</span>
      </div>
    </section>

    <section class="card card--front" aria-label="Card front">
      <div class="brand">
        <span class="brand-square"></span>
        <span class="brand-name">Parcels &amp; Petals</span>
      </div>
      <div class="color-stripe">
        <span class="s1"></span><span class="s2"></span><span class="s3"></span><span class="s4"></span>
        <span class="s5"></span><span class="s6"></span><span class="s7"></span>
      </div>
      <div class="blue-band">
        <div class="holder">
          <p class="holder-name">Ritu Malhotra</p>
          <p class="holder-address">C-17, Dilkusha Marg<br>Lucknow - 226014</p>
        </div>
        <div class="divider"></div>
        <ul class="contacts">
          <li>
            <svg viewBox="0 0 16 16" aria-hidden="true"><rect x="4" y="1" width="8" height="14" rx="1.5" fill="none" stroke="#fff" stroke-width="1.6"/><circle cx="8" cy="12.3" r="0.9" fill="#fff"/></svg>
            +9450012873
          </li>
          <li>
            <svg viewBox="0 0 16 16" aria-hidden="true"><rect x="1" y="3" width="14" height="10" rx="1" fill="none" stroke="#fff" stroke-width="1.6"/><path d="M1.5 3.8 8 9l6.5-5.2" fill="none" stroke="#fff" stroke-width="1.6"/></svg>
            ritumal47@postbright.example
          </li>
          <li>
            <svg viewBox="0 0 16 16" aria-hidden="true"><circle cx="8" cy="8" r="6.5" fill="none" stroke="#fff" stroke-width="1.4"/><ellipse cx="8" cy="8" rx="2.8" ry="6.5" fill="none" stroke="#fff" stroke-width="1.2"/><path d="M1.5 8h13" stroke="#fff" stroke-width="1.2"/></svg>
            www.parcelspetals.example
          </li>
        </ul>
      </div>
    </section>
  </main>
</body>
</html>
```